Boat Dealership Needs A Post Boat Show Sale Flyer - 8.5X11

We need an 8.5X11 flyer to hand out at our boat show to promote a sale at our dealership following our boat show.

Annual Post Boat Show Open House

February 25 - March 5
Extended Hours
Friday, February 25 - 9 AM to 6 PM
Saturday, February 26 -9 AM to 6 PM
Sunday, February 27 - 11 AM to 3 PM
Monday, February 28 through Friday, March 4 - 9 AM to 6 PM
Saturday, March 5 - 9 AM to 3 PM
After hours by appointment

Phone - (555) 314-2671
Website – callowayboats.example

Didn't buy at the show? Wondering what to do after the show?
Don't miss your last chance to secure boat show season pricing.
Our three large, indoor showrooms are fully stocked, and our discounted boat show pricing continues.
Extended hours and continued show pricing.
In-stock incentives and special financing.
New pontoons in-stock starting at $25,995 and less than $150 a month with approved credit.
New tritoons in stock starting at $38,995 and less than $250 a month with approved credit.
Side console Ripley Hull fishing boats starting at $17,995 and less than $125 a month with approved credit.
Special pricing on remaining in-stock Corvales.
Save thousands on Tidewell.

Family-owned relaxed atmosphere.
Refreshments provided.
Prefer to shop virtually? Shop 24/7 on our website at callowayboats.example or set up a real-time video call.

Proudly Offering – Calloway, Marlo, Ashdowne, and WaveDrift Pontoons, Corvale, Kelaro, Tidewell, Ripley Hull

We would like our brand logos on the design.

Follow Us On Chatterly, Snapverse, and Vidorama

Colors
FFF300
FFF600
FEFA6F
FFFEC7
FFFEE8
FFC000
F8CF3A
FAE287
FDF2CF
FEFAEE
F0912C
F2A743
F7CA91
FBE8D2
FDF5EE
EE7325
F08F49
F5BC92
FAE3D3
FDF4ED
EB3D1F
EC4F4E
F09395
F8D3D4
FCEDEE

```html
<!DOCTYPE html>
<html lang="en">
<head>
<meta charset="utf-8">
<title>Calloway Boating – Annual Post Boat Show Open House</title>
<link rel="stylesheet" href="https://fonts.googleapis.com/css2?family=Anton&family=Archivo:ital,wght@1,800&family=Hind:wght@300;400;600&display=swap">
<style>
  :root {
    --stage: #262626;
    --navy: #0d0c2e;
    --white: #ffffff;
    --ink: #0b0b0b;
    --red: #eb3d1f;
    --frame-red: #e0262e;
    --placeholder: #3a3960;
    --sky: #9cc3e6;
    --water: #5b84a8;
    --muted: #dcdcf0;
    --social: #8fb6de;
  }
  * { box-sizing: border-box; margin: 0; padding: 0; }
  html, body { width: 1200px; height: 800px; overflow: hidden; background: var(--stage); }
  .flyer {
    position: absolute; left: 295px; top: 5px;
    width: 610px; height: 790px;
    background: var(--navy);
    font-family: "Hind", sans-serif;
    overflow: hidden;
  }
  .header { position: absolute; left: 0; top: 0; width: 610px; height: 128px;
    display: flex; align-items: center; justify-content: center; gap: 14px; }
  .brand-mark { width: 60px; height: 60px; border-radius: 50%; background: var(--placeholder); }
  .brand-name { font-family: "Hind", sans-serif; font-weight: 600; color: var(--white);
    font-size: 28px; letter-spacing: 4px; line-height: 1; text-transform: uppercase; }
  .hero { position: absolute; left: 0; top: 128px; width: 610px; height: 256px;
    background: linear-gradient(180deg, #c7dcef 0%, var(--sky) 45%, var(--water) 62%, #46698c 100%); }
  .hero-title { position: absolute; left: 78px; top: 11px; width: 440px; height: 238px;
    background: var(--white); text-align: center; font-family: "Anton", sans-serif; color: var(--ink);
    display: flex; flex-direction: column; justify-content: center; }
  .hero-title .kicker { font-size: 33px; line-height: 1.1; }
  .hero-title .headline { font-size: 70px; line-height: 1; }
  .hero-title .sub { font-size: 36px; line-height: 1.15; }
  .hero-title .dates { font-size: 29px; line-height: 1.3; color: var(--red); }
  .hours-band { position: absolute; left: 0; top: 394px; width: 610px; height: 147px; background: var(--white); }
  .photo { position: absolute; top: 0; height: 147px;
    background: linear-gradient(180deg, #dbe8f4 0%, #a9c8e4 45%, #5f8bb2 70%, #4a7397 100%); }
  .photo.left { left: 0; width: 182px; }
  .photo.right { left: 429px; width: 181px; }
  .hours { position: absolute; left: 192px; top: 2px; width: 234px; }
  .hours h2 { font-family: "Archivo", sans-serif; font-style: italic; font-weight: 800;
    font-size: 24px; color: var(--ink); line-height: 1.2; }
  .hours ul { list-style: none; font-size: 12.3px; line-height: 17.6px; color: #222; }
  .hours b { color: var(--red); font-weight: 600; }
  .offers { position: absolute; left: 17px; top: 559px; width: 576px; height: 189px;
    border: 2px solid var(--frame-red); padding: 10px 16px; }
  .offers ul { list-style: none; color: var(--muted); font-size: 10.4px; line-height: 16.9px; font-weight: 300; }
  .footer { position: absolute; left: 28px; top: 755px; width: 560px; height: 26px;
    display: flex; align-items: center; color: var(--white); font-weight: 600; font-size: 13.5px; }
  .contact { display: flex; align-items: center; gap: 8px; margin-right: 42px; }
  .contact svg { width: 18px; height: 18px; }
  .socials { display: flex; gap: 14px; margin-left: auto; }
  .socials span { width: 19px; height: 19px; border-radius: 50%; background: var(--social); }
</style>
</head>
<body>
<main class="flyer">
  <header class="header">
    <span class="brand-mark"></span>
    <span class="brand-name">Calloway Boating</span>
  </header>

  <section class="hero" role="img" aria-label="Photo of a red wake boat cruising on a lake under a blue sky">
    <div class="hero-title">
      <span class="kicker">Annual Post</span>
      <span class="headline">Boat Show</span>
      <span class="sub">Open House</span>
      <span class="dates">February 25 – March 5</span>
    </div>
  </section>

  <section class="hours-band">
    <div class="photo left" role="img" aria-label="Photo of friends on a pontoon boat on the water"></div>
    <div class="hours">
      <h2>Extended Hours</h2>
      <ul>
        <li>Friday, February 25 - <b>9 AM</b> to <b>6 PM</b></li>
        <li>Saturday, February 26 - <b>9 AM</b> to <b>6 PM</b></li>
        <li>Sunday, February 27 - <b>11 AM</b> to <b>3 PM</b></li>
        <li>Monday, February 28 through Friday,<br>March 4 - <b>9 AM</b> to <b>6 PM</b></li>
        <li>Saturday, March 5 - <b>9 AM</b> to <b>3 PM</b></li>
      </ul>
    </div>
    <div class="photo right" role="img" aria-label="Photo of people jumping from a red sport boat into a lake"></div>
  </section>

  <section class="offers">
    <ul>
      <li>Didn't buy at the show? Wondering what to do after the show?</li>
      <li>Don't miss your last chance to secure boat show season pricing.</li>
      <li>Our three large, indoor showrooms are fully stocked, and our discounted boat show pricing continues.</li>
      <li>Extended hours and continued show pricing.</li>
      <li>In-stock incentives and special financing.</li>
      <li>New pontoons in-stock starting at $25,995 and less than $150 a month with approved credit.</li>
      <li>New tritoons in stock starting at $38,995 and less than $250 a month with approved credit.</li>
      <li>Side console Ripley Hull fishing boats starting at $17,995 and less than $125 a month with approved credit.</li>
      <li>Special pricing on remaining in-stock Corvales.</li>
      <li>Save thousands on Tidewell.</li>
    </ul>
  </section>

  <footer class="footer">
    <span class="contact">
      <svg viewBox="0 0 24 24" fill="none" stroke="#8fb6de" stroke-width="2" stroke-linecap="round"><path d="M5 3h4l2 5-2.5 1.5a11 11 0 0 0 6 6L16 13l5 2v4a2 2 0 0 1-2 2A17 17 0 0 1 3 5a2 2 0 0 1 2-2z"/></svg>
      (555) 314-2671
    </span>
    <span class="contact">
      <svg viewBox="0 0 24 24" fill="none" stroke="#8fb6de" stroke-width="2" stroke-linecap="round"><path d="M10 14a5 5 0 0 0 7 0l3-3a5 5 0 0 0-7-7l-1 1"/><path d="M14 10a5 5 0 0 0-7 0l-3 3a5 5 0 0 0 7 7l1-1"/></svg>
      CALLOWAYBOATS.EXAMPLE
    </span>
    <span class="socials" aria-label="Social channels">
      <span></span><span></span><span></span><span></span><span></span>
    </span>
  </footer>
</main>
</body>
</html>
```